Volt'n Electrical Business Card Design

FRONT OF CARD: should highlight the company logo ( please use image attached) and in small font in the bottom corner must have REC 48193

BACK OF CARD : Company logo at the top, underneath the logo have my name Owen Tate under my name in smaller font Qualified Electrician.
Details to also include are Mobile: 0438257109 E-mail: voltnelectrical@mailbox-example.net

Front and back of card please try to use similar colours as used in the logo. (Blues, greys, black and white)

The logo was created on this website so if you need a different file type of the logo please notify me.

Thanks, Owen

Industry/Entity Type

Business

Contact Information for Business Card

Details are in project description.

Colors
3176b5

Requirements
Must have
• Company logo and contact details

```html
<!DOCTYPE html>
<html lang="en">
<head>
<meta charset="utf-8">
<title>Volt'n Electrical Business Card</title>
<link rel="stylesheet" href="https://fonts.googleapis.com/css2?family=Lato:wght@400;700&family=Tinos&display=swap">
<style>
  :root {
    --backdrop: #2f2a27;
    --card-back: #1d1d1f;
    --card-front: #121214;
    --accent: #3fb4ea;
    --logo-blue: #2a86c4;
    --text-light: #f2f2f2;
    --text-muted: #a9a9ab;
    --text-dim: #6b6b6e;
  }
  html, body {
    margin: 0;
    padding: 0;
    width: 1200px;
    height: 844px;
    overflow: hidden;
    background: var(--backdrop);
    font-family: "Lato", sans-serif;
  }
  .stage {
    position: relative;
    width: 1200px;
    height: 844px;
  }
  .card {
    position: absolute;
    top: 272px;
    width: 520px;
    height: 300px;
    overflow: hidden;
    box-shadow: 0 10px 30px rgba(0,0,0,0.45);
  }

  /* Back side: name and contact details */
  .card-back {
    left: 50px;
    background: linear-gradient(110deg, var(--card-back) 55%, #2a2a2c 100%);
  }
  .band {
    position: absolute;
    left: 0;
    width: 100%;
    background: var(--accent);
  }
  .band-top { top: 0; height: 12px; }
  .band-bottom { bottom: 0; height: 16px; }
  .identity {
    position: absolute;
    top: 52px;
    left: 0;
    width: 100%;
    text-align: center;
  }
  .person-name {
    display: inline-block;
    margin: 0;
    padding: 0 4px 4px;
    font-size: 19px;
    font-weight: 700;
    letter-spacing: 0.5px;
    color: var(--text-light);
    text-transform: uppercase;
    border-bottom: 1px solid var(--accent);
  }
  .person-role {
    margin: 4px 0 0;
    font-size: 14px;
    color: var(--text-dim);
  }
  .contact-list {
    position: absolute;
    top: 134px;
    left: 0;
    width: 100%;
    margin: 0;
    padding: 0;
    list-style: none;
    text-align: center;
    font-size: 14.5px;
    line-height: 19px;
    color: var(--text-muted);
  }
  .address {
    position: absolute;
    bottom: 36px;
    left: 0;
    width: 100%;
    margin: 0;
    text-align: center;
    font-size: 14.5px;
    color: var(--text-muted);
  }

  /* Front side: company name */
  .card-front {
    left: 630px;
    background: radial-gradient(ellipse at 50% 30%, #26282b 0%, var(--card-front) 60%);
  }
  .tab {
    position: absolute;
    width: 14px;
    height: 44px;
    background: var(--accent);
  }
  .tab-left { left: 0; top: 150px; }
  .tab-right { right: 0; top: 36px; }
  .company-name {
    position: absolute;
    top: 112px;
    left: 0;
    width: 100%;
    margin: 0;
    text-align: center;
    font-size: 40px;
    font-weight: 700;
    letter-spacing: 3px;
    text-transform: uppercase;
    color: var(--logo-blue);
  }
  .licence {
    position: absolute;
    right: 22px;
    bottom: 52px;
    margin: 0;
    font-family: "Tinos", serif;
    font-size: 17px;
    color: var(--logo-blue);
  }
</style>
</head>
<body>
  <main class="stage">
    <section class="card card-back" aria-label="Business card back">
      <div class="band band-top"></div>
      <div class="identity">
        <h1 class="person-name">Marcus Hale</h1>
        <p class="person-role">Managing Director</p>
      </div>
      <ul class="contact-list">
        <li>044-318-2604</li>
        <li>123-902-4417</li>
        <li>contact@sampledomain.net</li>
        <li>www.sampledomain.net</li>
      </ul>
      <p class="address">5678 Harbour Street | Country Name, AB | 654321</p>
      <div class="band band-bottom"></div>
    </section>

    <section class="card card-front" aria-label="Business card front">
      <div class="tab tab-left"></div>
      <div class="tab tab-right"></div>
      <h2 class="company-name">Volt'n Electrical</h2>
      <p class="licence">REC 48193</p>
    </section>
  </main>
</body>
</html>
```